Automotive Accessories Business Card

Design a business template that match our new logo design and our industry.

https://www.kelvorauto.com/

Target Market(s)

Aftermarket auto parts and accessories

Industry/Entity Type

automotive

Contact Information for Business Card

company logo

Font styles to use
Serif
Sans Serif

Colors
EB3D1F
EC4F4E
F09395
F8D3D4
FCEDEE

```html
<!DOCTYPE html>
<html lang="en">
<head>
<meta charset="utf-8">
<title>Kelvor Auto Supply – Business Card</title>
<link rel="stylesheet" href="https://fonts.googleapis.com/css2?family=Open+Sans:wght@400;600;800&display=swap">
<style>
  :root {
    --bg: #e9e6e3;
    --paper: #ffffff;
    --paper-shade: #f2f2f2;
    --charcoal: #3a3a3c;
    --charcoal-deep: #2a2a2c;
    --back-card: #3b3b3d;
    --back-mark: #2c2c2e;
    --red: #e53036;
    --red-deep: #c81f26;
    --text-light: #f2f2f2;
    --text-soft: #d8d8d8;
  }
  * { box-sizing: border-box; margin: 0; padding: 0; }
  html, body { width: 1200px; height: 960px; overflow: hidden; }
  body {
    background: var(--bg);
    font-family: "Open Sans", Arial, sans-serif;
    display: flex;
    flex-direction: column;
    align-items: center;
    justify-content: center;
    gap: 60px;
  }
  .card {
    position: relative;
    width: 700px;
    height: 400px;
    overflow: hidden;
    box-shadow: 0 6px 18px rgba(0,0,0,0.18);
  }
  .card-art { position: absolute; inset: 0; }

  /* back */
  .card-back {
    background: radial-gradient(ellipse at 40% 35%, #4a4a4c 0%, var(--back-card) 55%, #2f2f31 100%);
    display: flex; align-items: center; justify-content: center;
  }
  .back-brand { display: flex; align-items: center; gap: 14px; }
  .back-brand .mark { width: 22px; height: 22px; background: var(--back-mark); }
  .back-brand .name {
    font-weight: 800; font-size: 64px; letter-spacing: 4px;
    color: var(--back-mark);
  }

  /* front */
  .card-front { background: var(--paper); }
  .front-brand {
    position: absolute; left: 56px; top: 52px;
    display: flex; align-items: center; gap: 12px;
  }
  .front-brand .mark { width: 18px; height: 18px; background: var(--red); }
  .front-brand .name {
    font-weight: 800; font-size: 46px; letter-spacing: 3px; color: var(--red); line-height: 1;
  }
  .front-brand .sub {
    position: absolute; left: 30px; top: 56px;
    font-weight: 800; font-size: 13px; letter-spacing: 2px; color: var(--red);
    white-space: nowrap;
  }
  .contact {
    position: absolute; right: 40px; top: 190px;
    text-align: right; color: var(--text-light);
  }
  .contact .person {
    font-weight: 800; font-size: 26px; letter-spacing: 1.5px; line-height: 1.1;
  }
  .contact .role {
    font-size: 16px; color: var(--text-soft); margin-bottom: 18px;
  }
  .contact ul { list-style: none; }
  .contact li {
    display: flex; justify-content: flex-end; align-items: center; gap: 10px;
    font-size: 17px; line-height: 1.6; color: var(--text-soft);
  }
  .contact li strong { font-weight: 800; font-style: italic; color: var(--text-light); }
  .contact .icon { width: 16px; height: 16px; flex: none; }
</style>
</head>
<body>

  <section class="card card-back" aria-label="Business card back">
    <div class="back-brand">
      <span class="mark"></span>
      <span class="name">KELVOR</span>
    </div>
  </section>

  <section class="card card-front" aria-label="Business card front">
    <svg class="card-art" viewBox="0 0 700 400" width="700" height="400" aria-hidden="true">
      <defs>
        <linearGradient id="panel" x1="0" y1="0" x2="1" y2="1">
          <stop offset="0" stop-color="#4a4a4c"/>
          <stop offset="0.5" stop-color="#3a3a3c"/>
          <stop offset="1" stop-color="#2a2a2c"/>
        </linearGradient>
      </defs>
      <rect class="paper" width="700" height="400" fill="#ffffff"/>
      <path class="dark-panel" d="M78 196 Q360 150 700 118 L700 360 L660 378 L78 378 Z" fill="url(#panel)"/>
      <path class="red-band" d="M0 158 L62 176 L78 196 L78 220 L0 220 Z" fill="#d2232a"/>
      <path class="band-shade" d="M0 220 L78 220 L78 378 L0 378 Z" fill="#f4f4f4"/>
      <line class="accent-line" x1="360" y1="162" x2="600" y2="128" stroke="#3a3a3c" stroke-width="2.5"/>
      <line class="red-line" x1="200" y1="360" x2="470" y2="360" stroke="#e53036" stroke-width="2.5"/>
    </svg>

    <div class="front-brand">
      <span class="mark"></span>
      <span class="name">KELVOR</span>
      <span class="sub">AUTO SUPPLY INC</span>
    </div>

    <div class="contact">
      <p class="person">MARCUS DALE</p>
      <p class="role">Sales Manager</p>
      <ul>
        <li>1-866-555-0148
          <svg class="icon" viewBox="0 0 16 16"><path d="M4 1 L6.5 4.5 L5 6 Q6.5 9.5 10 11 L11.5 9.5 L15 12 L13 15 Q4 14 1 3 Z" fill="#e53036"/></svg>
        </li>
        <li>sales@kelvorauto.com
          <svg class="icon" viewBox="0 0 16 16"><rect x="1" y="3" width="14" height="10" fill="#e53036"/><path d="M1 3 L8 9 L15 3" fill="none" stroke="#3a3a3c" stroke-width="1.2"/></svg>
        </li>
        <li><span>www.<strong>kelvorauto</strong>.com</span>
          <svg class="icon" viewBox="0 0 16 16"><circle cx="8" cy="8" r="7" fill="#e53036"/><path d="M1 8 H15 M8 1 V15 M3 4 Q8 6 13 4 M3 12 Q8 10 13 12" stroke="#3a3a3c" stroke-width="1" fill="none"/></svg>
        </li>
      </ul>
    </div>
  </section>

</body>
</html>
```